Weightloss company needs Business Card

We want a business card that is clean and professional, yet portrays that we are a friendly, innovative, and versatile program designed to fit the needs of our clients.
I would like there to be 2 sides, one side having an appointment card, and the other side containing the logo and business information. There can be decorations on both sides. The logo is attached.

Target Market(s)

Men and women 40-60

Industry/Entity Type

Business

Contact Information for Business Card

Font styles to use
Sans Serif

Requirements
Must have
• The logo, space for business information
Nice to have
• The colors in the logo
Should not have
• No pictures of people or food

```html
<!DOCTYPE html>
<html lang="en">
<head>
<meta charset="utf-8">
<title>Risewell Weightloss – Business Card</title>
<link rel="stylesheet" href="https://fonts.googleapis.com/css2?family=Source+Sans+3:ital,wght@0,400;0,600;1,400&display=swap">
<style>
  :root {
    --brand-red: #d3173c;
    --accent-cyan: #2fb9e3;
    --ink-grey: #505357;
    --dots: #8a8c90;
    --card-white: #f4f4f5;
    --backdrop: #d8d9db;
  }
  * { box-sizing: border-box; margin: 0; padding: 0; }
  html, body { width: 1105px; height: 1200px; overflow: hidden; }
  body {
    background: var(--backdrop);
    font-family: "Source Sans 3", "Helvetica Neue", Arial, sans-serif;
    color: var(--ink-grey);
    position: relative;
  }
  .card {
    position: absolute;
    left: 182px;
    width: 746px;
    height: 425px;
    background: var(--card-white);
  }
  .card--front { top: 119px; }
  .card--back { top: 637px; }

  /* Front */
  .brand {
    position: absolute;
    left: 440px;
    top: 72px;
    width: 270px;
    height: 80px;
    display: flex;
    align-items: center;
    gap: 12px;
    justify-content: flex-end;
  }
  .brand__dot {
    width: 18px; height: 18px; border-radius: 50%;
    background: var(--brand-red);
    flex: none;
  }
  .brand__name {
    color: var(--brand-red);
    font-weight: 600;
    font-size: 30px;
    line-height: 1.05;
    text-align: right;
  }
  .holder__name {
    position: absolute; left: 36px; top: 212px;
    color: var(--brand-red);
    font-weight: 600; font-size: 27px; letter-spacing: 0.5px;
  }
  .holder__title {
    position: absolute; left: 36px; top: 246px;
    color: var(--accent-cyan);
    font-size: 19px;
  }
  .holder__rule {
    position: absolute; left: 188px; top: 263px;
    width: 518px; height: 2px;
    background: var(--accent-cyan);
  }
  .contact-list {
    position: absolute; left: 36px; top: 286px;
    list-style: none;
  }
  .contact-list li {
    display: flex; align-items: center; gap: 10px;
    height: 28.7px;
    font-size: 19.5px;
  }
  .contact-list svg { width: 18px; height: 18px; fill: var(--brand-red); flex: none; }
  .address {
    position: absolute; right: 40px; top: 315px;
    text-align: right; font-size: 19.5px; line-height: 27.5px;
    font-style: normal;
  }
  .address__web { letter-spacing: 3px; }

  /* Back */
  .appointment__title {
    position: absolute; left: 0; right: 0; top: 32px;
    text-align: center;
    color: var(--brand-red);
    font-weight: 600; font-size: 27px;
  }
  .field {
    position: absolute;
    color: var(--brand-red);
    font-size: 20px;
    display: flex; align-items: flex-end; gap: 8px;
  }
  .field__line {
    border-bottom: 2px dotted var(--dots);
    height: 1px;
    margin-bottom: 5px;
  }
  .field--name { left: 43px; top: 100px; }
  .field--name .field__line { width: 568px; }
  .field--date { left: 43px; top: 160px; }
  .field--date .field__line { width: 284px; }
  .field--time { left: 418px; top: 160px; }
  .field--time .field__line { width: 146px; }
  .field__suffix { font-size: 15px; margin-bottom: 2px; }
  .field--note { left: 43px; top: 220px; }
  .field--note .field__line { width: 568px; }
  .note-line {
    position: absolute; left: 43px; width: 643px;
    border-bottom: 2px dotted var(--dots);
  }
  .note-line--1 { top: 281px; }
  .note-line--2 { top: 322px; }
  .policy {
    position: absolute; left: 0; right: 0; top: 350px;
    text-align: center;
    font-style: italic; font-size: 15.5px; line-height: 22px;
  }
</style>
</head>
<body>
  <section class="card card--front" aria-label="Business card front">
    <div class="brand">
      <span class="brand__dot"></span>
      <span class="brand__name">Risewell<br>Weightloss</span>
    </div>

    <h1 class="holder__name">DANIEL MERCER</h1>
    <p class="holder__title">CEO/FOUNDER</p>
    <div class="holder__rule"></div>

    <ul class="contact-list">
      <li>
        <svg viewBox="0 0 24 24" aria-hidden="true"><path d="M6.6 10.8a15.1 15.1 0 0 0 6.6 6.6l2.2-2.2a1 1 0 0 1 1-.25 11.4 11.4 0 0 0 3.6.57 1 1 0 0 1 1 1V20a1 1 0 0 1-1 1A17 17 0 0 1 3 4a1 1 0 0 1 1-1h3.5a1 1 0 0 1 1 1c0 1.25.2 2.45.57 3.57a1 1 0 0 1-.25 1z"/></svg>
        555 214 7730
      </li>
      <li>
        <svg viewBox="0 0 24 24" aria-hidden="true"><path d="M7 1h10a2 2 0 0 1 2 2v18a2 2 0 0 1-2 2H7a2 2 0 0 1-2-2V3a2 2 0 0 1 2-2zm0 3v14h10V4zm5 15.2a1.2 1.2 0 1 0 0 2.4 1.2 1.2 0 0 0 0-2.4z"/></svg>
        555 318 4492
      </li>
      <li>
        <svg viewBox="0 0 24 24" aria-hidden="true"><path d="M6 2h12v6H6zM3 9h18a2 2 0 0 1 2 2v7h-4v4H5v-4H1v-7a2 2 0 0 1 2-2zm4 8v3h10v-3z"/></svg>
        555 702 6185
      </li>
      <li>
        <svg viewBox="0 0 24 24" aria-hidden="true"><path d="M2 5h20v14H2zm2 2v.5l8 5 8-5V7l-8 5z"/></svg>
        hello@risewellfit.com
      </li>
    </ul>

    <address class="address">
      2140 Juniper Court<br>
      Fairbanks, Alaska 99701<br>
      <span class="address__web">www.risewellfit.com</span>
    </address>
  </section>

  <section class="card card--back" aria-label="Appointment card">
    <h2 class="appointment__title">Next Appointment</h2>

    <div class="field field--name"><span>Name :</span><span class="field__line"></span></div>
    <div class="field field--date"><span>Date :</span><span class="field__line"></span></div>
    <div class="field field--time"><span>Time :</span><span class="field__line"></span><span class="field__suffix">AM/PM</span></div>
    <div class="field field--note"><span>Note :</span><span class="field__line"></span></div>
    <div class="note-line note-line--1"></div>
    <div class="note-line note-line--2"></div>

    <p class="policy">Please give me 24 hours notice if you are unable to keep your appointment or<br>a cancellation fee may be charged.</p>
  </section>
</body>
</html>
```